"Lantern Field" Play - Poster Design for Theatre Group

We are an amateur theatre group based in Geneva, Switzerland. We take pride in eye-catching posters for our shows, which are printed in various sizes.
This design will be for a play in March 2016. The play is called "Lantern Field", and it's a Harwick Medal winner from Marcus Ellery-Pound. The play is about a couple who have everything a family could want, until they lose a child in a life-shattering accident that turns their world upside down. The play charts the couple's bittersweet search to find each other and to find comfort.
Most importantly, we want a design that will make people want to see the show. We don't want to give away the plot or be too heavy-handed about death, but we want it to be clear that it's not a comedy (although there are some lighter moments!).
Attached you will find a template for the poster. This simply has our group name and logo in the top right corner: (Lakeshore Stage Players Circle presents).
You may change the color of both the text and the logo, but please do not change the font, size, or location.
Here is the information that needs to be on the poster, wherever you see fit:
play title: Lantern Field
author byline: by Marcus Ellery-Pound
director line: directed by Rob Feltwick
tagline: How do you keep it together when your whole world's fallen apart?
dates and times:
1-5 March 2016
(Tue-Fri 20:00, Sat 19:00)
location:
Théâtre du Vieux-Moulin
Eaux-Vives, Geneva
websites:
www.lspc.ch
www.scenelettres.ch
Technical Details:
Any font or combination of fonts is acceptable. The largest text should be the play title. The author's name must be at least 50% of the title font size.
For this competition, we would like the version with A3 proportions, which will also be used at F4 (89.5 x 128 cm) and A5 sizes (14.8 x 21 cm). Therefore no text should be below 9pt at A5.
However, from the winning designer we will also need repurposed sizes of the same design. Here is a comprehensive list of the sizes we will need.
1) A3 print poster. Artwork should be 300dpi, CMYK, sent with a 1mm bleed all round, to specification PDF/X-1A:2001. We will need this image in PDF format in addition to the default Artbrigade formats.
2) Chatterly advert picture. 1200px by 628px, RGB jpeg. This must comply with Chatterly’s restrictions on amount of text, which is no more than 20% of area taken up by text.(https://www.chatterly.example/ads/tools/text_overlay).
Because of these restrictions it is sufficient to include just the title and the author's name in this version.
3) Chatterly cover picture: 851px by 314px. RGB jpeg. It is sufficient to include just the title and the author's name in this version.
4) Web banner. 1000px by 300px. RGB jpeg. This version should include just the main image(s), no text.
Theatergoers
Entertainment

```html
<!DOCTYPE html>
<html lang="en">
<head>
<meta charset="utf-8">
<title>Lantern Field — Poster</title>
<link rel="stylesheet" href="https://fonts.googleapis.com/css2?family=Playfair+Display:wght@700&family=Libre+Baskerville:ital,wght@1,700&family=Open+Sans:wght@400;600;700;800&display=swap">
<style>
  :root {
    --ink: #000000;
    --paper: #ffffff;
    --glow-core: #fbf1dc;
    --glow-warm: #c9b48e;
    --tunnel-mid: #5e5140;
    --tunnel-deep: #1c1813;
    --soft-text: #e8e4dc;
  }
  * { margin: 0; padding: 0; box-sizing: border-box; }
  html, body { width: 867px; height: 1200px; overflow: hidden; background: var(--ink); }
  .poster {
    position: relative;
    width: 867px;
    height: 1200px;
    overflow: hidden;
    background: var(--ink);
    color: var(--paper);
    font-family: "Open Sans", Arial, sans-serif;
  }
  .tunnel-photo {
    position: absolute;
    inset: 0;
    background:
      radial-gradient(ellipse 120px 150px at 640px 560px, var(--glow-core) 0%, rgba(251,241,220,0.85) 35%, rgba(201,180,142,0) 100%),
      radial-gradient(ellipse 340px 380px at 610px 580px, rgba(201,180,142,0.75) 0%, rgba(94,81,64,0.65) 45%, rgba(28,24,19,0.4) 75%, rgba(0,0,0,0) 100%),
      radial-gradient(ellipse 580px 520px at 540px 600px, var(--tunnel-deep) 0%, var(--ink) 80%);
  }
  .presenter {
    position: absolute;
    top: 30px;
    right: 32px;
    display: flex;
    align-items: center;
    gap: 14px;
  }
  .presenter-name {
    text-align: right;
    font-weight: 700;
    font-size: 15px;
    line-height: 1.2;
    color: var(--paper);
  }
  .presenter-mark {
    width: 62px;
    height: 62px;
    border-radius: 50%;
    background: var(--paper);
  }
  .play-title {
    position: absolute;
    top: 220px;
    left: 0;
    width: 100%;
    text-align: center;
    font-family: "Playfair Display", "Times New Roman", serif;
    font-weight: 700;
    font-size: 96px;
    line-height: 1;
    letter-spacing: 1px;
    text-transform: uppercase;
  }
  .author {
    position: absolute;
    top: 322px;
    left: 0;
    width: 100%;
    text-align: center;
    font-weight: 800;
    font-size: 28px;
    text-transform: uppercase;
    letter-spacing: 0.5px;
  }
  .author .by { text-transform: none; font-weight: 700; }
  .tagline {
    position: absolute;
    top: 862px;
    left: 0;
    width: 100%;
    text-align: center;
    font-family: "Libre Baskerville", Georgia, serif;
    font-style: italic;
    font-weight: 700;
    font-size: 24px;
    line-height: 1.4;
  }
  .credits {
    position: absolute;
    top: 1006px;
    left: 0;
    width: 100%;
    text-align: center;
    line-height: 1.25;
  }
  .director-label { font-size: 14px; color: var(--soft-text); }
  .director-name { font-size: 16px; font-weight: 700; text-transform: uppercase; letter-spacing: 0.5px; }
  .details {
    position: absolute;
    top: 1060px;
    left: 0;
    width: 100%;
    text-align: center;
    font-size: 12px;
    line-height: 1.3;
    color: var(--soft-text);
  }
  .details p + p { margin-top: 6px; }
  .details .venue { font-weight: 700; font-size: 14px; color: var(--paper); }
  .details .web { font-size: 11px; }
</style>
</head>
<body>
  <main class="poster">
    <div class="tunnel-photo" role="img" aria-label="Photograph of a dark tunnel glowing with light at its end, two silhouetted figures standing apart"></div>

    <header class="presenter">
      <p class="presenter-name">Lakeshore Stage<br>Players Circle<br>presents</p>
      <span class="presenter-mark" aria-hidden="true"></span>
    </header>

    <h1 class="play-title">Lantern Field</h1>
    <p class="author"><span class="by">by</span> Marcus Ellery-Pound</p>

    <p class="tagline">How do you keep it together<br>when your whole world’s fallen apart?</p>

    <div class="credits">
      <p class="director-label">directed by</p>
      <p class="director-name">Rob Feltwick</p>
    </div>

    <div class="details">
      <p>March 1 - 5 2016<br>(Tue - Fri 20:00, Sat 19:00)</p>
      <p class="venue">Théâtre du Vieux-Moulin<br>Eaux-Vives, Geneva</p>
      <p class="web">www.lspc.ch<br>www.scenelettres.ch</p>
    </div>
  </main>
</body>
</html>
```